New Business Card Design Project

We are looking for a talented individual to create a truly awesome/unique business card design for us. We are looking for a someone to design something that will really stand out from the crowd - we don't mind what ideas you come up with (ie embossed/flat/matte/shine etc etc) just wow us with your creativity.
Updates

Target Market(s)

Video Games Industry Professionals (all levels of seniority from QA Testers through to CEOs)

Contact Information for Business Card

Company logo (see upload)
Company name: Northbay Play Careers Ltd
Employee Name: Darren Elsby
Job title: CEO
Website: www.nbpc2go.example
Office +44 1632 960418
Mobile: +44 7700 900276
Email: darren@nbpc2go.example

Colors

Designer to choose colors to be used in the design.

Requirements
Must have
• The business card design MUST contain all the information listed in the BUSINESS CARD DETAILS box.
• You will see the colours that are relevant to us (ie company logo) in the uploaded imagery - however you do not have to use all these colours when designing the business card itself
• MUST BE DOUBLE SIDED

```html
<!DOCTYPE html>
<html lang="en">
<head>
<meta charset="utf-8">
<title>Northbay Play Careers – Business Card</title>
<link rel="stylesheet" href="https://fonts.googleapis.com/css2?family=Saira+Semi+Condensed:wght@300;700&family=Mulish:wght@400;600&display=swap">
<style>
  :root{
    --navy:#1f2a5c;
    --orange:#e0700f;
    --band:#c5c8d2;
    --paper:#ffffff;
    --text:#2b2f45;
    --stage:#e8edf0;
  }
  *{margin:0;padding:0;box-sizing:border-box}
  html,body{width:1200px;height:900px;overflow:hidden;background:var(--stage)}
  .stage{position:relative;width:1200px;height:900px}
  .card{position:absolute;left:270px;width:660px;height:377px;background:var(--paper);
        overflow:hidden;box-shadow:0 10px 30px rgba(20,40,60,.18);font-family:"Mulish",sans-serif;color:var(--text)}
  .card--front{top:52px}
  .card--back{top:471px}
  .bands{position:absolute;inset:0}
  .brand{position:absolute;display:flex;align-items:center;gap:12px;white-space:nowrap;
         font-family:"Saira Semi Condensed",sans-serif;font-weight:700;color:var(--navy)}
  .brand__dot{flex:none;width:30px;height:30px;border-radius:50%;background:var(--navy)}
  .card--front .brand{right:34px;top:56px;font-size:28px;line-height:1}
  .holder{position:absolute;left:40px;top:98px;font-family:"Saira Semi Condensed",sans-serif;line-height:1}
  .holder__name{font-size:32px;font-weight:700;color:var(--navy);letter-spacing:.5px}
  .holder__name span{color:var(--orange)}
  .holder__role{font-size:20px;font-weight:300;color:var(--orange);margin-top:4px}
  .contacts{position:absolute;left:78px;top:180px;list-style:none}
  .contacts li{display:flex;align-items:center;gap:12px;height:28px;font-size:15px;line-height:1;white-space:nowrap}
  .icon{flex:none;width:24px;height:24px;border:2px solid var(--orange);display:flex;align-items:center;justify-content:center;background:var(--paper)}
  .icon svg{width:14px;height:14px}
  .address{position:absolute;left:230px;top:312px;display:flex;gap:12px;align-items:center;font-size:13px;line-height:1.35;white-space:nowrap}
  .card--back .brand{left:50%;top:50%;transform:translate(-50%,-50%);font-size:40px;line-height:1}
  .card--back .brand__dot{width:40px;height:40px}
  .web{position:absolute;right:34px;bottom:26px;font-size:15px;letter-spacing:4px;color:var(--navy);font-weight:600;white-space:nowrap}
</style>
</head>
<body>
<main class="stage">
  <section class="card card--front" aria-label="Business card front">
    <svg class="bands" viewBox="0 0 660 377" aria-hidden="true">
      <rect x="0" y="18" width="660" height="12" fill="var(--band)"/>
      <rect x="0" y="38" width="660" height="6" fill="var(--band)"/>
      <rect x="0" y="166" width="520" height="8" fill="var(--band)"/>
      <rect x="0" y="191" width="60" height="6" fill="var(--band)"/>
      <rect x="0" y="219" width="60" height="6" fill="var(--band)"/>
      <rect x="0" y="247" width="60" height="6" fill="var(--band)"/>
      <rect x="0" y="275" width="60" height="6" fill="var(--band)"/>
      <rect x="0" y="298" width="520" height="8" fill="var(--band)"/>
    </svg>
    <div class="brand"><span class="brand__dot"></span>Northbay Play Careers</div>
    <div class="holder">
      <div class="holder__name">DARREN <span>ELSBY</span></div>
      <div class="holder__role">CEO</div>
    </div>
    <ul class="contacts">
      <li><span class="icon"><svg viewBox="0 0 16 16"><path d="M3 2l3 0 1 3-2 1c1 2 2 3 4 4l1-2 3 1v3c-6 0-10-4-10-10z" fill="none" stroke="var(--navy)" stroke-width="1.3"/></svg></span>+44 1632 960418</li>
      <li><span class="icon"><svg viewBox="0 0 16 16"><rect x="4" y="1.5" width="8" height="13" rx="1.5" fill="none" stroke="var(--navy)" stroke-width="1.3"/><circle cx="8" cy="12.3" r=".9" fill="var(--navy)"/></svg></span>+44 7700 900276</li>
      <li><span class="icon"><svg viewBox="0 0 16 16"><rect x="1.5" y="3.5" width="13" height="9" fill="none" stroke="var(--navy)" stroke-width="1.3"/><path d="M1.5 3.5l6.5 5 6.5-5" fill="none" stroke="var(--navy)" stroke-width="1.3"/></svg></span>darren@nbpc2go.example</li>
      <li><span class="icon"><svg viewBox="0 0 16 16"><circle cx="8" cy="8" r="6.3" fill="none" stroke="var(--navy)" stroke-width="1.3"/><ellipse cx="8" cy="8" rx="2.8" ry="6.3" fill="none" stroke="var(--navy)" stroke-width="1.1"/><path d="M1.7 8h12.6" stroke="var(--navy)" stroke-width="1.1"/></svg></span>www.nbpc2go.example</li>
    </ul>
    <div class="address">
      <span class="icon"><svg viewBox="0 0 16 16"><path d="M8 15s5-5 5-8.5a5 5 0 0 0-10 0C3 10 8 15 8 15z" fill="none" stroke="var(--navy)" stroke-width="1.3"/><circle cx="8" cy="6.5" r="1.8" fill="none" stroke="var(--navy)" stroke-width="1.2"/></svg></span>
      <p>Northbay Play Careers Ltd<br>The Mill House, Harbour Lane<br>Eastcombe, Northbay, NB4 2QT, United Kingdom</p>
    </div>
  </section>

  <section class="card card--back" aria-label="Business card back">
    <svg class="bands" viewBox="0 0 660 377" aria-hidden="true">
      <rect x="0" y="92" width="660" height="14" fill="var(--orange)"/>
      <rect x="0" y="118" width="660" height="3" fill="var(--orange)"/>
      <rect x="0" y="256" width="660" height="3" fill="var(--orange)"/>
      <rect x="0" y="271" width="660" height="14" fill="var(--orange)"/>
    </svg>
    <div class="brand"><span class="brand__dot"></span>Northbay Play Careers</div>
    <div class="web">WWW.NBPC2GO.EXAMPLE</div>
  </section>
</main>
</body>
</html>
```